Basic Company webpage with the elements and colors of our Logo

Basic Home page with a few pages:
- Home,
- About US,
- Contact us
- Services

Target Market(s)

Business Customers (B2B)

Coding

Coded - Design and coding required

Number of Pages Required

5+ page

Requirements
Must have
• Professional, Clean, Simple High Tech, Contact should have a contact us dialog for sending messages to us
Nice to have
• Meet with us links for calendar access though MS Bookings

```html
<!DOCTYPE html>
<html lang="en">
<head>
<meta charset="utf-8">
<title>Meridian Tech Services Group</title>
<link href="https://fonts.googleapis.com/css2?family=Montserrat:wght@500;600;700;800&family=Inter:wght@400;500;600&family=Tinos&display=swap" rel="stylesheet">
<style>
:root{
  --navy:#0b4a70;
  --navy-deep:#073957;
  --hero-dark:#0a1f4a;
  --orange:#f6ab3a;
  --ink:#1f2630;
  --muted:#5a6470;
  --white:#ffffff;
  --field:#ffffff;
}
*{box-sizing:border-box;margin:0;padding:0}
html,body{width:1200px;height:4197px;overflow:hidden}
body{position:relative;background:var(--white);font-family:"Inter",sans-serif;color:var(--ink)}
.abs{position:absolute}
h2.section-title{position:absolute;left:0;width:1200px;text-align:center;font-family:"Montserrat",sans-serif;font-weight:700;font-size:33px;color:var(--navy);letter-spacing:.5px}

/* header */
.site-header{top:0;left:0;width:1200px;height:93px;background:var(--white)}
.brand{left:110px;top:28px;font-family:"Montserrat",sans-serif;font-weight:700;font-size:26px;color:var(--navy);display:flex;align-items:center;gap:10px}
.brand .dot{width:14px;height:14px;border-radius:50%;background:var(--orange)}
.topbar{left:0;top:0;width:1200px;height:47px}
.topbar-text{top:14px;font-size:15px;color:var(--white);display:flex;align-items:center;gap:12px}
.icon-circle{width:30px;height:30px;border-radius:50%;background:var(--white);display:flex;align-items:center;justify-content:center}
.main-nav{top:62px;left:512px;display:flex;gap:0;font-family:"Montserrat",sans-serif;font-weight:500;font-size:15px;color:#111}
.main-nav a{color:inherit;text-decoration:none;position:absolute;white-space:nowrap}
.main-nav a.active{color:var(--navy)}

/* hero */
.hero{top:93px;left:0;width:1200px;height:640px;overflow:hidden;background:linear-gradient(100deg,#0b2a5c 0%,#0a1c48 45%,#07143a 100%)}
.hero-visual{right:0;top:0;width:620px;height:600px;background:radial-gradient(circle at 75% 45%,rgba(60,170,220,.55) 0%,rgba(140,70,200,.35) 30%,rgba(10,30,80,0) 65%)}
.hero-kicker{left:110px;top:128px;font-family:"Montserrat",sans-serif;font-weight:700;font-size:23px;color:var(--white)}
.hero-title{left:110px;top:166px;font-family:"Montserrat",sans-serif;font-weight:700;font-size:51px;line-height:61px;color:var(--white)}
.hero-text{left:110px;top:290px;width:470px;font-size:15px;line-height:31px;color:#e3e9f5}
.btn-light{background:var(--white);color:var(--navy);font-family:"Montserrat",sans-serif;font-weight:700;font-size:16px;display:flex;align-items:center;justify-content:center;border-radius:2px}
.hero .btn-light{left:110px;top:367px;width:152px;height:47px;color:#0a1c48}

/* why */
.why-text{left:125px;top:906px;width:950px;text-align:center;font-size:15px;line-height:31px;color:#333}
.feature{top:995px;width:170px;text-align:center}
.feature svg{display:block;margin:0 auto}
.feature p{margin-top:14px;font-family:"Tinos",serif;font-size:20px;color:#111}

/* about */
.about{top:1203px;left:0;width:1200px;height:583px;background:linear-gradient(90deg,#0d3f62,#0b4a70 60%,#0c4d73)}
.about-photo{left:120px;top:79px;width:428px;height:428px;border-radius:50%;border:8px solid var(--white);background:linear-gradient(150deg,#cfd8e2,#9aa8b5 55%,#6f7f8e)}
.about h2{position:absolute;left:640px;top:96px;font-family:"Montserrat",sans-serif;font-weight:700;font-size:33px;color:var(--white)}
.about-text{left:599px;top:165px;width:486px;font-size:15px;line-height:31px;color:#e6eef5}
.about .btn-light{left:599px;top:438px;width:134px;height:47px}

/* services */
.service-card{top:1996px;width:316px;height:332px;background:var(--white);border-radius:8px;box-shadow:0 4px 14px rgba(0,0,0,.12);overflow:hidden;border-bottom:6px solid var(--navy)}
.service-photo{width:100%;height:246px}
.service-card h3{text-align:center;margin-top:30px;font-family:"Montserrat",sans-serif;font-weight:600;font-size:17px;color:#111}
.service-card.featured{height:490px;border:none;background:var(--orange);padding:0 14px 14px}
.featured .service-photo{margin:0 -14px;width:calc(100% + 28px)}
.featured .inner{background:var(--white);height:230px;border-radius:0 0 8px 8px;text-align:center}
.featured h3{margin-top:0;padding-top:24px;color:var(--orange)}
.featured li{list-style:none;font-size:15px;line-height:31px;color:#222}
.featured ul{margin-top:6px}
.arrow-btn{width:24px;height:24px;border-radius:50%;border:1.5px solid #666;display:flex;align-items:center;justify-content:center}

/* testimonials */
.testimonials{top:2574px;left:0;width:1200px;height:625px;background:linear-gradient(90deg,#0b3f63,#0b4a70)}
.testimonials h2{color:var(--white)}
.t-card{top:194px;width:310px;height:330px;border:3px solid var(--white);border-radius:6px;padding:22px 24px}
.stars{color:var(--orange);font-size:16px;letter-spacing:2px}
.t-card p{margin-top:10px;font-size:14px;line-height:26px;color:#e8eef4;text-align:justify}
.t-divider{position:absolute;left:24px;right:24px;top:217px;height:1px;background:rgba(255,255,255,.45)}
.t-avatar{position:absolute;left:24px;top:241px;width:55px;height:55px;border-radius:50%;background:linear-gradient(135deg,#d9cbb8,#9e8e7c)}
.t-name{position:absolute;left:96px;top:242px;font-family:"Roboto",sans-serif;font-weight:700;font-size:18px;color:var(--white)}
.t-place{position:absolute;left:96px;top:270px;font-size:15px;color:#d4dee8}
.arrow-solid{width:38px;height:38px;border-radius:50%;display:flex;align-items:center;justify-content:center}

/* contact */
.field{background:var(--field);box-shadow:0 3px 10px rgba(0,0,0,.14);border-radius:3px;padding:17px 17px;font-size:14px;color:#666}
.btn-submit{left:531px;top:3634px;width:136px;height:52px;background:var(--navy);color:var(--white);font-family:"Montserrat",sans-serif;font-weight:700;font-size:16px;display:flex;align-items:center;justify-content:center;border-radius:2px}

/* footer */
.site-footer{top:3784px;left:0;width:1200px;height:413px;background:var(--navy-deep)}
.footer-brand{left:109px;top:103px;font-family:"Montserrat",sans-serif;font-weight:700;font-size:25px;color:var(--white);display:flex;align-items:center;gap:10px}
.footer-brand .dot{width:14px;height:14px;border-radius:50%;background:var(--orange)}
.footer-col h4{font-family:"Montserrat",sans-serif;font-weight:600;font-size:21px;color:var(--white);margin-bottom:8px}
.footer-col li{list-style:none;font-size:15px;line-height:31px;color:var(--white);display:flex;align-items:center;gap:10px}
.footer-contact{display:flex;align-items:center;gap:14px;font-size:15px;color:var(--white);position:absolute;left:0;white-space:nowrap}
.footer-contact .ic{width:36px;height:36px;border-radius:50%;background:#0d5a86;display:flex;align-items:center;justify-content:center}
.footer-rule{left:99px;top:338px;width:1002px;height:1px;background:rgba(255,255,255,.5)}
.copyright{left:0;top:364px;width:1200px;text-align:center;font-size:15px;color:var(--white)}
</style>
</head>
<body>

<header class="site-header abs">
  <svg class="topbar abs" width="1200" height="47" viewBox="0 0 1200 47"><polygon points="431,0 1200,0 1200,47 482,47" fill="#0b4a70"/></svg>
  <div class="brand abs"><span class="dot"></span>Meridian Tech</div>
  <div class="topbar-text abs" style="left:543px">
    <span class="icon-circle"><svg width="16" height="16" viewBox="0 0 24 24"><path d="M6.6 10.8a15.1 15.1 0 0 0 6.6 6.6l2.2-2.2c.3-.3.7-.4 1-.2 1.1.4 2.3.6 3.6.6.6 0 1 .4 1 1V20c0 .6-.4 1-1 1A17 17 0 0 1 3 4c0-.6.4-1 1-1h3.5c.6 0 1 .4 1 1 0 1.3.2 2.5.6 3.6.1.3 0 .7-.2 1z" fill="#0b4a70"/></svg></span>
    +1 555 010 2040
  </div>
  <div class="topbar-text abs" style="left:765px">
    <span class="icon-circle"><svg width="16" height="16" viewBox="0 0 24 24"><path d="M3 6h18v12H3z" fill="#0b4a70"/><path d="M3 6l9 7 9-7" stroke="#fff" stroke-width="1.6" fill="none"/></svg></span>
    hello@meridiantechgroup.com
  </div>
  <nav class="main-nav abs">
    <a class="active" style="left:0">HOME</a>
    <a style="left:123px">ABOUT US</a>
    <a style="left:279px">CONTACT US</a>
    <a style="left:455px">SERVICES</a>
  </nav>
</header>

<section class="hero abs">
  <div class="hero-visual abs" role="img" aria-label="Glowing digital globe with circuit lines"></div>
  <div class="hero-kicker abs">WELCOME TO</div>
  <h1 class="hero-title abs">MERIDIAN TECH<br>SERVICES GROUP</h1>
  <p class="hero-text abs">Lorem ipsum dolor sit amet, consectetur adipiscing elit, sed do eiusmod tempor incididunt ut labore et dolore magna aliqua.</p>
  <a class="btn-light abs">MEET WITH US</a>
  <svg class="abs" style="left:0;top:500px" width="1200" height="140" viewBox="0 0 1200 140">
    <path d="M0 110 Q600 -40 1200 110 L1200 140 L0 140 Z" fill="#fff" transform="translate(0,0)"/>
    <path d="M0 10 Q600 220 1200 10 L1200 140 L0 140 Z" fill="#fff"/>
    <path d="M40 40 Q600 200 1200 10 Q600 160 40 40 Z" fill="#f6ab3a"/>
  </svg>
</section>

<h2 class="section-title" style="top:830px">WHY CHOOSE US</h2>
<p class="why-text abs">Lorem ipsum dolor sit amet, consectetur adipiscing elit, sed do eiusmod tempor incididunt ut labore et dolore magna aliqua. Ut enim ad minim veniam, quis nostrud exercitation ullamco laboris nisi ut aliquip ex ea commodo consequat.</p>

<div class="feature abs" style="left:165px">
  <svg width="56" height="56" viewBox="0 0 56 56" fill="none" stroke="#222" stroke-width="2"><rect x="4" y="30" width="48" height="4"/><rect x="8" y="34" width="14" height="18"/><line x1="46" y1="34" x2="46" y2="52"/><rect x="12" y="10" width="14" height="18"/><rect x="36" y="18" width="8" height="12"/></svg>
  <p>Lorem ipsum</p>
</div>
<div class="feature abs" style="left:397px">
  <svg width="56" height="56" viewBox="0 0 56 56" fill="none" stroke="#222" stroke-width="2"><rect x="12" y="4" width="32" height="40"/><line x1="18" y1="14" x2="38" y2="14"/><line x1="18" y1="22" x2="38" y2="22"/><circle cx="24" cy="38" r="10"/><line x1="31" y1="45" x2="40" y2="53"/></svg>
  <p>Lorem ipsum</p>
</div>
<div class="feature abs" style="left:629px">
  <svg width="56" height="56" viewBox="0 0 56 56" fill="none" stroke="#222" stroke-width="2"><circle cx="28" cy="14" r="9"/><circle cx="14" cy="40" r="9"/><circle cx="42" cy="40" r="9"/><path d="M22 22 L18 31 M34 22 L38 31 M23 40 H33"/></svg>
  <p>Lorem ipsum</p>
</div>
<div class="feature abs" style="left:861px">
  <svg width="56" height="56" viewBox="0 0 56 56" fill="none" stroke="#222" stroke-width="2"><rect x="26" y="4" width="16" height="22"/><line x1="30" y1="10" x2="38" y2="10"/><line x1="30" y1="16" x2="38" y2="16"/><circle cx="12" cy="38" r="6"/><path d="M2 54 a10 10 0 0 1 20 0"/><circle cx="44" cy="38" r="6"/><path d="M34 54 a10 10 0 0 1 20 0"/><path d="M22 40 H32 M28 36 L32 40 L28 44"/></svg>
  <p>Lorem ipsum</p>
</div>

<section class="about abs">
  <div class="about-photo abs" role="img" aria-label="Two colleagues reviewing a tablet in an office"></div>
  <h2>ABOUT US</h2>
  <p class="about-text abs">Sed ut perspiciatis unde omnis iste natus error sit voluptatem accusantium doloremque laudantium, totam rem aperiam, eaque ipsa quae ab illo inventore veritatis et quasi architecto beatae vitae dicta sunt explicabo. Nemo enim ipsam voluptatem quia voluptas sit aspernatur aut odit aut fugit, sed quia consequuntur magni dolores eos qui ratione voluptatem sequi nesciunt. Neque porro quisquam est, qui dolorem ipsum quia dolor sit amet, consectetur, adipisci velit, dolore magnam aliquam quaerat voluptatem.</p>
  <a class="btn-light abs">Read More</a>
</section>

<h2 class="section-title" style="top:1900px">OUR SERVICES</h2>
<div class="arrow-btn abs" style="left:48px;top:2126px"><svg width="10" height="10" viewBox="0 0 10 10"><path d="M6.5 1 L2.5 5 L6.5 9" stroke="#444" stroke-width="1.5" fill="none"/></svg></div>
<div class="arrow-btn abs" style="left:1128px;top:2126px"><svg width="10" height="10" viewBox="0 0 10 10"><path d="M3.5 1 L7.5 5 L3.5 9" stroke="#444" stroke-width="1.5" fill="none"/></svg></div>

<article class="service-card abs" style="left:99px">
  <div class="service-photo" role="img" aria-label="Professional reviewing documents at a desk" style="background:linear-gradient(160deg,#e8ecef,#b9c2c9 60%,#6f7880)"></div>
  <h3>Excepteur sint occaecat</h3>
</article>
<article class="service-card featured abs" style="left:441px">
  <div class="service-photo" role="img" aria-label="Business handshake across a meeting table" style="background:linear-gradient(160deg,#d9d3cc,#a79d92 55%,#5d5a57)"></div>
  <div class="inner">
    <h3>Excepteur sint occaecat</h3>
    <ul><li>Brand Development</li><li>Marketing</li><li>Ad Campaigns</li><li>Recruiting</li><li>Interviews and Onboarding</li></ul>
  </div>
</article>
<article class="service-card abs" style="left:785px">
  <div class="service-photo" role="img" aria-label="Two analysts viewing data screens at night" style="background:linear-gradient(160deg,#2c3e55,#1a2536 60%,#4a6d8a)"></div>
  <h3>Excepteur sint occaecat</h3>
</article>

<section class="testimonials abs">
  <h2 class="section-title" style="top:100px;color:#fff">CLIENT&nbsp; TESTIMONIALS</h2>
  <div class="arrow-solid abs" style="left:41px;top:357px;border:1.5px solid #fff"><svg width="12" height="12" viewBox="0 0 10 10"><path d="M6.5 1 L2.5 5 L6.5 9" stroke="#fff" stroke-width="1.6" fill="none"/></svg></div>
  <div class="arrow-solid abs" style="left:1130px;top:357px;background:#fff"><svg width="12" height="12" viewBox="0 0 10 10"><path d="M3.5 1 L7.5 5 L3.5 9" stroke="#0b4a70" stroke-width="1.6" fill="none"/></svg></div>

  <article class="t-card abs" style="left:109px">
    <div class="stars">★★★★★</div>
    <p>Lorem ipsum dolor sit amet, consectetur adipiscing elit, sed do eiusmod tempor incididunt ut labore et dolore magna aliqua ut enim ad minim veniam, quis nostrud exercitation ullamco.</p>
    <div class="t-divider"></div>
    <div class="t-avatar" role="img" aria-label="Client portrait"></div>
    <div class="t-name">Daniel Reyes</div>
    <div class="t-place">Florida, United States</div>
  </article>
  <article class="t-card abs" style="left:444px">
    <div class="stars">★★★★★</div>
    <p>Lorem ipsum dolor sit amet, consectetur adipiscing elit, sed do eiusmod tempor incididunt ut labore et dolore magna aliqua ut enim ad minim veniam, quis nostrud exercitation ullamco.</p>
    <div class="t-divider"></div>
    <div class="t-avatar" role="img" aria-label="Client portrait"></div>
    <div class="t-name">Marta</div>
    <div class="t-place">Florida, United States</div>
  </article>
  <article class="t-card abs" style="left:781px">
    <div class="stars">★★★★★</div>
    <p>Lorem ipsum dolor sit amet, consectetur adipiscing elit, sed do eiusmod tempor incididunt ut labore et dolore magna aliqua ut enim ad minim veniam, quis nostrud exercitation ullamco.</p>
    <div class="t-divider"></div>
    <div class="t-avatar" role="img" aria-label="Client portrait"></div>
    <div class="t-name">Owen Castell</div>
    <div class="t-place">Florida, United States</div>
  </article>
</section>

<h2 class="section-title" style="top:3317px">CONTACT US</h2>
<div class="field abs" style="left:182px;top:3399px;width:411px;height:49px">Name</div>
<div class="field abs" style="left:606px;top:3399px;width:411px;height:49px">Email</div>
<div class="field abs" style="left:182px;top:3463px;width:411px;height:49px">Phone Number</div>
<div class="field abs" style="left:606px;top:3463px;width:411px;height:49px">Subject</div>
<div class="field abs" style="left:182px;top:3525px;width:835px;height:86px">Message</div>
<a class="btn-submit abs">Submit</a>

<footer class="site-footer abs">
  <div class="footer-brand abs"><span class="dot"></span>Meridian Tech</div>
  <div class="footer-col abs" style="left:443px;top:70px">
    <h4>Quick Links</h4>
    <ul>
      <li><svg width="13" height="13" viewBox="0 0 12 12"><path d="M1 6H10M6 2L10 6L6 10" stroke="#fff" stroke-width="2" fill="none"/></svg>Home</li>
      <li><svg width="13" height="13" viewBox="0 0 12 12"><path d="M1 6H10M6 2L10 6L6 10" stroke="#fff" stroke-width="2" fill="none"/></svg>About Us</li>
      <li><svg width="13" height="13" viewBox="0 0 12 12"><path d="M1 6H10M6 2L10 6L6 10" stroke="#fff" stroke-width="2" fill="none"/></svg>Services</li>
      <li><svg width="13" height="13" viewBox="0 0 12 12"><path d="M1 6H10M6 2L10 6L6 10" stroke="#fff" stroke-width="2" fill="none"/></svg>Contact Us</li>
    </ul>
  </div>
  <div class="footer-col abs" style="left:625px;top:70px">
    <h4>Other Links</h4>
    <ul>
      <li><svg width="13" height="13" viewBox="0 0 12 12"><path d="M1 6H10M6 2L10 6L6 10" stroke="#fff" stroke-width="2" fill="none"/></svg>FAQ</li>
      <li><svg width="13" height="13" viewBox="0 0 12 12"><path d="M1 6H10M6 2L10 6L6 10" stroke="#fff" stroke-width="2" fill="none"/></svg>Terms of Use</li>
      <li><svg width="13" height="13" viewBox="0 0 12 12"><path d="M1 6H10M6 2L10 6L6 10" stroke="#fff" stroke-width="2" fill="none"/></svg>Privacy Policy</li>
      <li><svg width="13" height="13" viewBox="0 0 12 12"><path d="M1 6H10M6 2L10 6L6 10" stroke="#fff" stroke-width="2" fill="none"/></svg>Support Links</li>
      <li><svg width="13" height="13" viewBox="0 0 12 12"><path d="M1 6H10M6 2L10 6L6 10" stroke="#fff" stroke-width="2" fill="none"/></svg>Conditions</li>
    </ul>
  </div>
  <div class="footer-col abs" style="left:847px;top:70px;width:300px;height:220px">
    <h4>Contact Us</h4>
    <div class="footer-contact" style="top:55px"><span class="ic"><svg width="14" height="16" viewBox="0 0 14 18"><path d="M7 0a7 7 0 0 1 7 7c0 5-7 11-7 11S0 12 0 7a7 7 0 0 1 7-7z" fill="#fff"/><circle cx="7" cy="7" r="2.5" fill="#0d5a86"/></svg></span>Company Name, United States.</div>
    <div class="footer-contact" style="top:115px"><span class="ic"><svg width="16" height="12" viewBox="0 0 18 12"><rect width="18" height="12" fill="#fff"/><path d="M0 0l9 7 9-7" stroke="#0d5a86" stroke-width="1.5" fill="none"/></svg></span>contact@meridiantechgroup.com</div>
    <div class="footer-contact" style="top:175px"><span class="ic"><svg width="15" height="15" viewBox="0 0 24 24"><path d="M6.6 10.8a15.1 15.1 0 0 0 6.6 6.6l2.2-2.2c.3-.3.7-.4 1-.2 1.1.4 2.3.6 3.6.6.6 0 1 .4 1 1V20c0 .6-.4 1-1 1A17 17 0 0 1 3 4c0-.6.4-1 1-1h3.5c.6 0 1 .4 1 1 0 1.3.2 2.5.6 3.6.1.3 0 .7-.2 1z" fill="#fff"/></svg></span>+1 555 010 2040</div>
  </div>
  <div class="footer-rule abs"></div>
  <p class="copyright abs">Copyrights@2025. Meridian Tech Services Group. All Rights Reserved</p>
</footer>

</body>
</html>
```